Luxury Baseline Grove/academy - Webdesign

We want to develop a cutting edge website for a luxury tennis academy. Academy is based in Russia and includes all the necessary amenities for comfortable stay: apartments, spa, tennis courts, training facilities, etc.
We would like to see a clean, simple and modern design (with implementation of all the current trends in web design, although our project has to be distinct and unique).
Color scheme: we would like to see colors present in our logos and all the current associated with tennis. We are open to your ideas and creativity on this front.
The final design should communicate simplicity, be user friendly and convey premium feel.
We woud like to see unique ideas in the design, unconventional techniques, etc.
We don't want standard template design!
Updates
We want to mention that this Tennis Academy has a light focus on nature, as the new material we have uploaded illustrates.
Additional comment to everyone!
We couldn't upload this file to the system: it is too big.
Thank you everyone for your submissions!
Industry/Entity Type
Training
Requirements
Must have
- We would like to see the designs for the following pages:
Home Page:
- Slideshow
- Short description and all the standard stuff
About Us:
- Description with some images
Services:
- Simple description of all of the provided services and possibility to book all of them on the website
! Important ! Develop small system for booking of the days of stay and registration for the courses
Booking and registration !
News:
- Creative layout to display recent news of the academy
Coaches:
- Image and short description of our staff.
Club / Gallery:
- Images and descriptions of the amenities in the territory.
We want a unique display of images: not just lines and rows filled with images
- One idea: an interactive map that displays images and description on mouseover or click on the object on the map (but again, we are open to all your ideas)
Contacts:
- Contact form, contacts, etc.
Sport Store:
- Basic layout for the goods and services provided by the sports store located in the academy
Prices:
- Price lists and ranges with a button leading to registration and booking
For pages like About Us and Services, it would be enough to develop one unified layout for all of them.

```html
<!DOCTYPE html>
<html lang="en">
<head>
<meta charset="utf-8">
<title>Baseline Grove – Tennis Academy</title>
<link rel="stylesheet" href="https://fonts.googleapis.com/css2?family=Oswald:wght@300;400;500;600&family=Arimo:ital,wght@0,400;1,400&display=swap">
<style>
:root{
  --green:#2e9e43;
  --green-dark:#1e7a32;
  --lime:#c8d800;
  --yellow:#e6d400;
  --text:#6b6b6b;
  --muted:#8a8a8a;
  --rule:#9a9a9a;
  --nav-bg:#efefef;
  --nav-line:#dcdcdc;
  --ink:#222;
}
*{margin:0;padding:0;box-sizing:border-box}
html,body{width:1029px;height:1200px;overflow:hidden;background:#fff}
body{position:relative;font-family:"Arimo",Arial,sans-serif;color:var(--text)}
.abs{position:absolute}
.brand{left:130px;top:38px;display:flex;align-items:center;gap:8px}
.brand__name{font-family:"Oswald",sans-serif;font-weight:500;font-size:38px;color:var(--green);letter-spacing:.5px}
.brand__dot{width:30px;height:30px;border-radius:50%;background:var(--lime)}
.call{right:128px;top:32px;display:flex;gap:6px;align-items:flex-start;font-family:"Oswald",sans-serif;color:#333;font-size:15px;line-height:16px;font-weight:400}
.nav{left:121px;top:111px;width:788px;height:66px;background:var(--nav-bg);display:flex}
.nav a{font-family:"Oswald",sans-serif;font-size:12.5px;color:#333;text-decoration:none;text-transform:uppercase;display:flex;align-items:flex-end;justify-content:center;padding-bottom:13px;border-left:1px solid var(--nav-line);flex:auto}
.nav a.is-home{flex:0 0 97px;border:0;background:linear-gradient(#3aa43c,#c9d600);color:#fff;flex-direction:column;align-items:center}
.nav a.is-home svg{margin-bottom:6px}
.slider{left:121px;top:177px;width:788px;height:223px;border:3px solid var(--green);border-top:0;background:linear-gradient(160deg,#8ea838 0%,#5f8e23 45%,#3e6c17 100%)}
.slider__quote{left:38px;top:70px;font-family:"Oswald",sans-serif;color:#fff;font-size:28px;line-height:1}
.slider__amp{color:var(--yellow);font-size:50px;font-weight:300;vertical-align:-10px}
.slider__game{left:110px;top:126px;font-family:"Oswald",sans-serif;color:#fff;font-size:30px}
.arrow{top:95px;width:22px;height:44px;background:var(--yellow)}
.arrow--l{left:-3px;border-radius:0 22px 22px 0}
.arrow--r{right:-3px;border-radius:22px 0 0 22px}
.dots{right:22px;top:199px;display:flex;gap:13px;align-items:center}
.dots i{width:6px;height:6px;border-radius:50%;background:#111;display:block}
.dots i.on{width:9px;height:9px;background:none;border:2px solid #111}
.feature{top:408px;width:250px}
.feature__img{height:120px;border:3px solid var(--green)}
h2{font-family:"Oswald",sans-serif;font-weight:300;color:var(--green);font-size:19px;text-transform:uppercase;line-height:1}
h2 b,h3 b{font-weight:500}
.feature h2{margin-top:15px}
.feature p{margin-top:10px;font-size:10px;line-height:9.7px}
.btn{display:inline-block;background:var(--green);color:#fff;font-family:"Oswald",sans-serif;font-weight:500;font-size:10.5px;padding:3px 4px;letter-spacing:.3px;text-transform:uppercase}
.feature .btn{margin-top:11px}
.rule{left:121px;width:788px;height:1px;background:var(--rule)}
h3{font-family:"Oswald",sans-serif;font-weight:300;color:var(--green);font-size:19px;line-height:1;padding-bottom:4px}
.col{width:250px}
.col--ruled h3{border-bottom:1px solid var(--green)}
.col p{font-size:9.6px;line-height:12px;margin-top:11px}
.news p{line-height:16px;color:var(--muted);font-size:9.5px}
.news p+p{margin-top:16px}
.list{list-style:none;margin-top:11px}
.list li{font-size:9.5px;line-height:19.3px;color:var(--muted);padding-left:14px;position:relative}
.list li::before{content:"";position:absolute;left:1px;top:7px;border-left:5px solid transparent;border-bottom:5px solid #999}
.services{display:grid;grid-template-columns:130px 120px}
.signup__img{width:212px;height:52px;border:2px solid var(--green);background:radial-gradient(circle at 40% 50%,#d9e63a,#7c9a18 70%,#3e4a10);margin-top:14px}
.signup__input{margin-top:8px;width:158px;height:22px;border:1px solid #bbb;font-size:9.5px;color:#222;padding:5px 9px;background:linear-gradient(#fff,#eee)}
.signup .btn{margin-top:8px;font-size:12px;padding:3px 5px}
.quote{font-style:italic;color:#999;font-size:9.5px;line-height:11.3px;margin-top:10px!important;width:210px}
.quote__by{font-family:"Oswald",sans-serif;font-weight:500;color:var(--ink);font-size:12px;text-align:right;width:210px;margin-top:10px}
.footer{left:0;top:1033px;width:1029px;height:167px}
.footer__row{left:136px;top:1125px;width:756px;font-family:"Oswald",sans-serif;color:#4a4a1a;font-size:16px;display:flex;align-items:center}
.social{display:flex;gap:8px;margin-left:10px}
.social i{display:block;width:26px;height:26px;background:#3a3a30}
</style>
</head>
<body>

<div class="abs brand"><span class="brand__name">Baseline Grove</span><span class="brand__dot"></span></div>

<div class="abs call">
  <svg width="26" height="30" viewBox="0 0 26 30" aria-hidden="true"><path d="M6 2c2 0 3 5 3 7s-3 2-3 4 4 8 6 9 3-2 5-2 6 2 6 4-3 5-6 5C9 29 1 16 2 7c0-3 2-5 4-5z" fill="#2e9e43"/></svg>
  <div>CALL US<br>+00.000.000.0000</div>
</div>

<nav class="abs nav">
  <a class="is-home" href="#"><svg width="22" height="22" viewBox="0 0 22 22" aria-hidden="true"><path d="M2 11 11 3l9 8M5 9v10h12V9" fill="none" stroke="#fff" stroke-width="2.4"/></svg>HOME</a>
  <a href="#">About us</a><a href="#">Services</a><a href="#">Booking</a><a href="#">Register</a><a href="#">News</a><a href="#">Coaches</a><a href="#">Gallery</a><a href="#">Prices</a><a href="#">Shop</a><a href="#">Contact us</a>
</nav>

<section class="abs slider" role="img" aria-label="Grass court close-up with a tennis ball on the baseline">
  <div class="abs slider__quote">“Play <span class="slider__amp">&amp;</span></div>
  <div class="abs slider__game">THE GAME!”</div>
  <span class="abs arrow arrow--l"></span>
  <span class="abs arrow arrow--r"></span>
  <div class="abs dots"><i></i><i></i><i class="on"></i><i></i><i></i></div>
</section>

<article class="abs feature" style="left:121px">
  <div class="feature__img" role="img" aria-label="Racket and balls on a hard court" style="background:linear-gradient(110deg,#9c2f4a 0%,#b0475a 40%,#2f9a55 60%,#3aa35c 100%)"></div>
  <h2><b>Match</b> Updates</h2>
  <p>Lorem Ipsum is simply dummy text of the printing and typesetting industry. Lorem Ipsum has been the indus-try's standard dummy text ever since the 1500s, when an unknown printer took a galley of type and scrambled it to make a type specimen book. It has survived not only five centuries, but also the leap into electronic typesetting, remaining essentially unchanged.</p>
  <span class="btn">Read more</span>
</article>
<article class="abs feature" style="left:389px">
  <div class="feature__img" role="img" aria-label="Three tennis balls resting on racket strings" style="background:radial-gradient(circle at 50% 55%,#d8d64a,#b8663e 60%,#a24e33)"></div>
  <h2><b>Player</b> Ratings</h2>
  <p>Lorem Ipsum is simply dummy text of the printing and typesetting industry. Lorem Ipsum has been the indus-try's standard dummy text ever since the 1500s, when an unknown printer took a galley of type and scrambled it to make a type specimen book. It has survived not only five centuries, but also the leap into electronic typesetting, remaining essentially unchanged.</p>
  <span class="btn">Read more</span>
</article>
<article class="abs feature" style="left:658px">
  <div class="feature__img" role="img" aria-label="Tennis ball against a racket on a green court" style="background:radial-gradient(circle at 65% 45%,#e8ec4a,#6fb06c 45%,#2f8a52)"></div>
  <h2><b>Best</b> Equipment</h2>
  <p>Lorem Ipsum is simply dummy text of the printing and typesetting industry. Lorem Ipsum has been the indus-try's standard dummy text ever since the 1500s, when an unknown printer took a galley of type and scrambled it to make a type specimen book. It has survived not only five centuries, but also the leap into electronic typesetting, remaining essentially unchanged.</p>
  <span class="btn">Read more</span>
</article>

<div class="abs rule" style="top:679px"></div>

<section class="abs col col--ruled" style="left:121px;top:694px">
  <h3><b>About</b> Northlane</h3>
  <p>Lorem Ipsum is simply dummy text of the printing and typesetting industry. Lorem Ipsum has been the indus-try's standard dummy text ever since the 1500s, when an unknown printer took a galley of type and scrambled it to make a type specimen book. It has survived not only five centuries.</p>
  <span class="btn" style="margin-top:35px">Read more</span>
</section>
<section class="abs col col--ruled news" style="left:389px;top:694px">
  <h3><b>Latest</b> News</h3>
  <p>Lorem Ipsum is simply dummy text of the printing and typesetting industry. Lorem Ipsum has been the indus-try's standard.</p>
  <p>Lorem Ipsum is simply dummy text of the printing and typesetting industry. Lorem Ipsum has been the indus-try's standard.</p>
</section>
<section class="abs col col--ruled" style="left:658px;top:694px">
  <h3><b>Our</b> Services</h3>
  <div class="services">
    <ul class="list"><li>Skin Care</li><li>New Arrivals</li><li>Make Up</li><li>Hair Care &amp; Styling</li><li>Nailing</li></ul>
    <ul class="list"><li>Bath &amp; Body</li><li>Fragrance</li><li>Organic &amp; Natural</li><li>For Men</li><li>Luxury Gifts</li></ul>
  </div>
</section>

<div class="abs rule" style="top:868px"></div>

<section class="abs col signup" style="left:121px;top:892px">
  <h3><b>News</b> Letter Sign Up</h3>
  <div class="signup__img" role="img" aria-label="Pile of tennis balls"></div>
  <div class="signup__input">Email Address</div>
  <span class="btn">Register</span>
</section>
<section class="abs col" style="left:389px;top:892px">
  <h3><b>Useful</b> links</h3>
  <ul class="list" style="margin-top:6px"><li>About Us</li><li>FAQ'S</li><li>Careers</li><li>Terms &amp; Coniditons</li><li>Privacy Policy</li></ul>
</section>
<section class="abs col" style="left:658px;top:892px">
  <h3><b>Testimonials</b></h3>
  <p class="quote">“Lorem Ipsum is simply dummy text of the print-ing and typesetting industry. Lorem Ipsum has been the industry's standard dummy text ever since the 1500s, when an unknown printer took a galley of type and scrambled it to make a type specimen book. It has survived not only five centuries.”</p>
  <div class="quote__by">Marcus Hale</div>
</section>

<svg class="abs footer" viewBox="0 0 1029 167" preserveAspectRatio="none" role="img" aria-label="Blurred close-up of a yellow tennis ball">
  <defs><linearGradient id="fball" x1="0" y1="0" x2="1" y2="1"><stop offset="0" stop-color="#d8c300"/><stop offset=".5" stop-color="#c9b400"/><stop offset="1" stop-color="#e8d800"/></linearGradient></defs>
  <polygon points="0,68 1029,0 1029,167 0,167" fill="url(#fball)"/>
</svg>

<div class="abs footer__row">
  <span>Customer Services Tel: 123-(456)-789</span>
  <span style="margin-left:38px">Copy Rights © Northlane Sport Ltd. 2012</span>
  <span style="margin-left:auto">Follow Us On:</span>
  <span class="social"><i></i><i></i><i></i></span>
</div>

</body>
</html>
```